Cobalt Margin Funds Bus card and Logo

I need a logo design and Bus card design. The fund focuses on evaluating and investing in minerals (sub-surface rights) and real estate.

Cobalt margin refers to a book of knowledge that each plebe gets when entering the Harwick Civic Academy (my alma mater)

Target Market(s)

Investors and financial advisors

Contact Information for Business Card

Simple - perhaps a logo with a theme on book of knowledge

Logo Text

Ex Scientia Imperium

Font styles to use
Serif
Sans Serif

Colors

Designer to choose colors to be used in the design.

Requirements
Must have
• memorable logo that is relatively simple

```html
<!DOCTYPE html>
<html lang="en">
<head>
<meta charset="utf-8">
<title>Cobalt Margin Funds — Business Card</title>
<link rel="stylesheet" href="https://fonts.googleapis.com/css2?family=Roboto:wght@400&display=swap">
<style>
  :root {
    --ink: #383838;
    --paper: #ffffff;
    --skyline-light: #ececec;
    --skyline-dark: #383838;
  }
  * { margin: 0; padding: 0; box-sizing: border-box; }
  html, body {
    width: 1200px;
    height: 565px;
    overflow: hidden;
    background: var(--paper);
    font-family: "Roboto", Arial, sans-serif;
  }
  .card {
    position: relative;
    width: 1200px;
    height: 565px;
    display: flex;
  }
  .card-front {
    position: relative;
    width: 600px;
    height: 100%;
    background: var(--paper);
  }
  .brand-mark {
    position: absolute;
    left: 262px;
    top: 86px;
    width: 76px;
    height: 76px;
    background: var(--ink);
  }
  .brand-name {
    position: absolute;
    left: 0;
    width: 600px;
    top: 226px;
    text-align: center;
    font-size: 44px;
    font-weight: 400;
    color: #111111;
    letter-spacing: 0.2px;
    text-transform: uppercase;
  }
  .skyline {
    position: absolute;
    left: 0;
    top: 352px;
    width: 600px;
    height: 180px;
    background: linear-gradient(to bottom, var(--skyline-light) 0%, #9a9a9a 45%, var(--skyline-dark) 100%);
  }
  .card-back {
    position: relative;
    width: 600px;
    height: 100%;
    background: var(--ink);
    color: var(--paper);
  }
  .back-title {
    position: absolute;
    left: 35px;
    top: 40px;
    font-size: 44px;
    font-weight: 400;
    text-transform: uppercase;
    white-space: nowrap;
  }
  .contact-row {
    position: absolute;
    left: 30px;
    display: flex;
    align-items: center;
    gap: 0;
  }
  .contact-icon {
    width: 36px;
    height: 36px;
    flex: none;
  }
  .contact-text {
    margin-left: 34px;
    font-size: 21px;
    line-height: 27px;
    text-transform: uppercase;
    white-space: nowrap;
  }
  .contact-text.web { text-transform: none; }
  .row-phone { top: 173px; }
  .row-web { top: 296px; }
  .row-address { top: 440px; }
</style>
</head>
<body>
  <main class="card">
    <section class="card-front">
      <div class="brand-mark" aria-hidden="true"></div>
      <h1 class="brand-name">Cobalt Margin Funds</h1>
      <div class="skyline" role="img" aria-label="City skyline silhouette in grey tones along the bottom edge"></div>
    </section>

    <section class="card-back">
      <h2 class="back-title">Cobalt Margin Funds</h2>

      <div class="contact-row row-phone">
        <svg class="contact-icon" viewBox="0 0 24 24" aria-hidden="true">
          <path fill="#ffffff" d="M6.6 10.8a15.1 15.1 0 0 0 6.6 6.6l2.2-2.2c.3-.3.7-.4 1-.2 1.1.4 2.3.6 3.6.6.6 0 1 .4 1 1V20c0 .6-.4 1-1 1A17 17 0 0 1 3 4c0-.6.4-1 1-1h3.5c.6 0 1 .4 1 1 0 1.3.2 2.5.6 3.6.1.3 0 .7-.2 1l-2.3 2.2z"/>
        </svg>
        <span class="contact-text">Cobalt Margin Funds</span>
      </div>

      <div class="contact-row row-web">
        <svg class="contact-icon" viewBox="0 0 24 24" aria-hidden="true">
          <g fill="none" stroke="#ffffff" stroke-width="1.8">
            <circle cx="12" cy="12" r="9.5"/>
            <ellipse cx="12" cy="12" rx="4.2" ry="9.5"/>
            <line x1="2.5" y1="12" x2="21.5" y2="12"/>
            <line x1="12" y1="2.5" x2="12" y2="21.5"/>
            <path d="M4 7h16M4 17h16"/>
          </g>
        </svg>
        <span class="contact-text web">www.cobalt_margin_funds.com</span>
      </div>

      <div class="contact-row row-address">
        <svg class="contact-icon" viewBox="0 0 24 24" aria-hidden="true">
          <path fill="#ffffff" d="M12 1.5a7 7 0 0 0-7 7c0 5 7 12.5 7 12.5s7-7.5 7-12.5a7 7 0 0 0-7-7zm0 9.7a2.7 2.7 0 1 1 0-5.4 2.7 2.7 0 0 1 0 5.4z"/>
          <ellipse cx="12" cy="22.3" rx="3.5" ry="1" fill="#ffffff"/>
        </svg>
        <span class="contact-text">14/C Larkmoor Street,<br>14/C Larkmoor Street Cross Road</span>
      </div>
    </section>
  </main>
</body>
</html>
```